Design for mobile and web app for sweepstakes.

We need the design for a mobile app (planned to be build with jquery mobile) and web app (mobile first, we will use same look and feel as mobile just with displaying more info at once).

The following pages must be included:
- Userregistration/Login (Reg via Email, Chattrove-Reg)

- List of available sweepstakes (including some icons: a video icon, a "like button" type icon, a "provide some info" type of icon) this should be on the side in wep app but in mobile app its a list. possible is also a mobile display where users can swipe back and forth through it.

- single sweepstake detailview . should present a single sweepstake and give users the opportunity to participate with a button.

user settings. (doesnt not have to include a lot of fields we will at ourself. should contain some datepicker (birthday), some on/off switch (receive newsletters) some textfield in order for us to have a feel.

We have included the following files:
- glimmorica_logo_final01.png:
this is our logo which should be used and also the look and feel must fit with the logo.

- glimmorica_logo_final06.png:
this is the app-icon

-folie neu login registrierung :
this is a simple mockup for a registration page. the design doesnt have to contain all fields we will do that ourselfes starting from your handover, but should represent a common registration page with some fields

- funktionalität mit hässlichen buttons )
this is just a mockup for a possible design. not that it does use our old logo. This again is not binding is just to get a feel for what we are looking for. A list of sweepstakes and a detailspage for the sweepstake for users to participate in it.

Target Market(s)

German speaking users, Austria, Germany, Switzerland
The app is adressing a wide crowd of users who are interested in participating in sweepstakes.

Industry/Entity Type

Build

Number of Pages Required

4 page

Font styles to use
Sans Serif

Requirements
Must have
• - jquery and jquery mobile
• - html5 (preferable bootstrap-based)
• - css3
• - description on used fonts and colors. fonts must be free to use and publicly available for anyone to use.
• - all buttons should be css

```html
<!DOCTYPE html>
<html lang="en">
<head>
<meta charset="utf-8">
<title>glimmorica – List of available sweepstakes</title>
<link rel="stylesheet" href="https://fonts.googleapis.com/css2?family=Quicksand:wght@500;600;700&display=swap">
<style>
  :root{
    --green:#7aab2b;
    --green-dark:#5e8a22;
    --black:#000;
    --white:#fff;
    --row-alt:#e8e8e8;
    --text:#111;
    --footer:#333333;
    --video:#26b56b;
    --like:#f2641e;
    --info:#18c6d6;
    --brand-square:#6aa12d;
    --yellow:#e7c32c;
    --yellow-dark:#c9a516;
  }
  *{margin:0;padding:0;box-sizing:border-box}
  html,body{width:1200px;height:2335px;overflow:hidden;background:var(--white)}
  body{font-family:"Quicksand",sans-serif;color:var(--text);position:relative}

  .status-bar{height:50px;background:var(--black);color:var(--white);display:flex;align-items:center;justify-content:space-between;padding:0 20px;font-size:32px;font-weight:600}
  .status-carrier{display:flex;align-items:flex-end;gap:6px}
  .status-right{display:flex;align-items:center;gap:14px}

  .app-header{height:270px;position:relative;background:var(--white)}
  .brand{position:absolute;left:35px;top:70px;display:flex;flex-direction:column;align-items:center;gap:14px}
  .brand-mark{width:110px;height:110px;background:var(--brand-square)}
  .brand-name{font-weight:700;font-size:62px;color:var(--green);line-height:1;letter-spacing:-1px}
  .menu-toggle{position:absolute;left:1042px;top:132px;width:92px;height:50px;display:flex;flex-direction:column;justify-content:space-between}
  .menu-toggle span{display:block;height:11px;border-radius:6px;background:var(--green)}

  .section-bar{height:120px;background:var(--black);display:flex;align-items:center;justify-content:space-between;padding:0 60px 0 90px}
  .section-title{color:var(--green);font-size:50px;font-weight:600}

  .sweepstake-list{list-style:none}
  .sweepstake{height:258px;position:relative;padding:25px 0 0 100px}
  .sweepstake:nth-child(even){background:var(--row-alt)}
  .sweepstake-title{color:var(--green);font-size:45px;font-weight:600;line-height:1.2}
  .sweepstake-text{margin-top:18px;width:850px;font-size:34px;font-weight:600;line-height:42px;hyphens:manual}
  .sweepstake-icon{position:absolute;left:1042px;top:76px;width:82px;height:92px}

  .filter-bar{height:147px;display:flex;justify-content:flex-start;align-items:center;padding-left:197px;gap:53px}
  .btn{width:350px;height:100px;border:none;border-radius:4px;font-family:"Quicksand",sans-serif;font-size:50px;font-weight:600;display:flex;align-items:center;justify-content:center}
  .btn-new{background:linear-gradient(var(--green),var(--green-dark));color:var(--white)}
  .btn-all{background:linear-gradient(#f0d23a,var(--yellow-dark));color:#111}

  .app-footer{position:absolute;left:0;top:2130px;width:1200px;height:205px;background:var(--footer);color:var(--white);font-size:35px;font-weight:600}
  .footer-copy{position:absolute;left:340px;top:72px}
  .footer-code{position:absolute;left:1080px;top:78px;font-size:32px}
</style>
</head>
<body>
  <div class="status-bar">
    <div class="status-carrier">
      <svg width="34" height="26" viewBox="0 0 34 26"><rect x="0" y="18" width="5" height="8" fill="#fff"/><rect x="7" y="13" width="5" height="13" fill="#fff"/><rect x="14" y="8" width="5" height="18" fill="#fff"/><rect x="21" y="4" width="5" height="22" fill="#fff"/><rect x="28" y="0" width="5" height="26" fill="#fff"/></svg>
      <span>Fonely</span>
    </div>
    <span>4:41 PM</span>
    <div class="status-right">
      <svg width="30" height="30" viewBox="0 0 30 30"><circle cx="15" cy="15" r="12" fill="none" stroke="#fff" stroke-width="3"/><path d="M15 8v8l5 3" stroke="#fff" stroke-width="3" fill="none"/></svg>
      <svg width="28" height="28" viewBox="0 0 28 28"><path d="M26 2 2 12l11 3 3 11z" fill="#fff"/></svg>
      <svg width="24" height="30" viewBox="0 0 24 30"><rect x="2" y="13" width="20" height="16" rx="2" fill="#fff"/><path d="M6 13V9a6 6 0 0 1 12 0v4" stroke="#fff" stroke-width="3" fill="none"/></svg>
      <svg width="60" height="28" viewBox="0 0 60 28"><rect x="1.5" y="1.5" width="52" height="25" rx="3" fill="none" stroke="#fff" stroke-width="3"/><rect x="55" y="9" width="4" height="10" fill="#fff"/><rect x="5" y="5" width="45" height="18" fill="#7dbd2f"/></svg>
    </div>
  </div>

  <header class="app-header">
    <div class="brand">
      <div class="brand-mark" role="img" aria-label="glimmorica brand mark"></div>
      <span class="brand-name">glimmorica</span>
    </div>
    <div class="menu-toggle" aria-label="Menu"><span></span><span></span><span></span></div>
  </header>

  <div class="section-bar">
    <h1 class="section-title">List of available sweepstakes</h1>
    <svg width="62" height="62" viewBox="0 0 62 62" aria-label="Search"><circle cx="24" cy="24" r="17" fill="none" stroke="#fff" stroke-width="5"/><path d="M37 37 56 56" stroke="#fff" stroke-width="8" stroke-linecap="round"/></svg>
  </div>

  <ul class="sweepstake-list">
    <li class="sweepstake">
      <h2 class="sweepstake-title">Duis aute irure dolor in reprehenderit</h2>
      <p class="sweepstake-text">It uses a dictionary of over 200 Latin words, com&shy;bined with a handful of model sentence</p>
      <svg class="sweepstake-icon" viewBox="0 0 82 92" aria-label="Video"><rect width="82" height="92" rx="6" fill="var(--video)"/><rect x="17" y="34" width="32" height="24" rx="4" fill="#fff"/><path d="M49 44 63 34v24L49 48z" fill="#fff"/></svg>
    </li>
    <li class="sweepstake">
      <h2 class="sweepstake-title">Duis aute irure dolor in reprehenderit</h2>
      <p class="sweepstake-text">It uses a dictionary of over 200 Latin words, com&shy;bined with a handful of model sentence</p>
      <svg class="sweepstake-icon" viewBox="0 0 82 92" aria-label="Like"><rect width="82" height="92" rx="6" fill="var(--like)"/><rect x="16" y="44" width="12" height="28" rx="2" fill="#fff"/><path d="M31 46 40 24c6 0 8 4 7 10l-2 8h14c4 0 6 4 5 7l-5 20c-1 3-3 4-6 4H31z" fill="#fff"/></svg>
    </li>
    <li class="sweepstake">
      <h2 class="sweepstake-title">Duis aute irure dolor in reprehenderit</h2>
      <p class="sweepstake-text">It uses a dictionary of over 200 Latin words, com&shy;bined with a handful of model sentence</p>
      <svg class="sweepstake-icon" viewBox="0 0 82 92" aria-label="Video"><rect width="82" height="92" rx="6" fill="var(--video)"/><rect x="17" y="34" width="32" height="24" rx="4" fill="#fff"/><path d="M49 44 63 34v24L49 48z" fill="#fff"/></svg>
    </li>
    <li class="sweepstake">
      <h2 class="sweepstake-title">Duis aute irure dolor in reprehenderit</h2>
      <p class="sweepstake-text">It uses a dictionary of over 200 Latin words, com&shy;bined with a handful of model sentence</p>
      <svg class="sweepstake-icon" viewBox="0 0 82 92" aria-label="Provide info"><rect width="82" height="92" rx="6" fill="var(--info)"/><path d="M22 18h28l12 12v44H22z" fill="none" stroke="#fff" stroke-width="4"/><path d="M30 42h24M30 52h24M30 62h24" stroke="#fff" stroke-width="4"/></svg>
    </li>
    <li class="sweepstake">
      <h2 class="sweepstake-title">Duis aute irure dolor in reprehenderit</h2>
      <p class="sweepstake-text">It uses a dictionary of over 200 Latin words, com&shy;bined with a handful of model sentence</p>
      <svg class="sweepstake-icon" viewBox="0 0 82 92" role="img" aria-label="glimmorica sweepstake"><rect width="82" height="92" rx="4" fill="var(--brand-square)"/></svg>
    </li>
    <li class="sweepstake">
      <h2 class="sweepstake-title">Duis aute irure dolor in reprehenderit</h2>
      <p class="sweepstake-text">It uses a dictionary of over 200 Latin words, com&shy;bined with a handful of model sentence</p>
      <svg class="sweepstake-icon" viewBox="0 0 82 92" aria-label="Video"><rect width="82" height="92" rx="6" fill="var(--video)"/><rect x="17" y="34" width="32" height="24" rx="4" fill="#fff"/><path d="M49 44 63 34v24L49 48z" fill="#fff"/></svg>
    </li>
  </ul>

  <div class="filter-bar">
    <button class="btn btn-new">Neu</button>
    <button class="btn btn-all">Alle</button>
  </div>

  <footer class="app-footer">
    <span class="footer-copy">glimmorica ©2014. Privacypolicy</span>
    <span class="footer-code">M1</span>
  </footer>
</body>
</html>
```